Product label for dietary supplement. Approx. 2.5 x 5.5 inches

I need a label for a nutraceutical dietary supplement. I have a pdf of an existing label for a different product and just need it updated, it needs a picture of red beets and garlic in the middle. I attached a document with the new copy. I think it is self explanatory. I also attached a file with a mock up of the label and right sizing.
I don't know what fonts were used in the existing label. Can you please try and match it as good as possible.

Target Market(s)

General public

Industry/Entity Type

Dietary Supplement

Colors
00AB8E
00BBA5
67D7C9
C6EFE9
E9F9F6

Requirements
Must have
• My customer wants a nice picture of beets and garlic on the front. That's the main ingredient of the capsules.
Nice to have
• I am also attaching a label for a different product, it should basically look the same.
Should not have
• No cartoon style, or anything drawn. It has to have a real picture.

```html
<!DOCTYPE html>
<html lang="en">
<head>
<meta charset="utf-8">
<title>Ruby Roots – Supplement Label</title>
<link rel="stylesheet" href="https://fonts.googleapis.com/css2?family=Oswald:wght@700&family=Cormorant+Garamond:ital,wght@1,500&family=Montserrat:wght@400;600;700&display=swap">
<style>
  :root {
    --stage: #2b2b2b;
    --paper: #ffffff;
    --brand-red: #e0173d;
    --leaf-green: #14a84a;
    --band-yellow: #e6e51c;
    --ink: #1c1c1c;
    --panel-black: #111111;
  }
  html, body {
    margin: 0;
    width: 1200px;
    height: 2218px;
    overflow: hidden;
    background: var(--stage);
  }
  .label {
    position: absolute;
    left: 50px;
    top: 858px;
    width: 1100px;
    height: 500px;
    display: block;
  }
  .body-copy { font-family: "Montserrat", Arial, sans-serif; font-size: 11.4px; fill: var(--ink); }
  .body-copy .strong { font-weight: 700; }
  .title { font-family: "Oswald", "Arial Narrow", sans-serif; font-weight: 700; font-size: 64px; fill: var(--brand-red); letter-spacing: 0.5px; }
  .tagline { font-family: "Cormorant Garamond", Georgia, serif; font-style: italic; font-weight: 500; font-size: 22px; fill: var(--brand-red); }
  .count { font-family: "Montserrat", Arial, sans-serif; fill: #fff; font-weight: 700; }
  .contact { font-family: "Montserrat", Arial, sans-serif; fill: #fff; font-size: 11px; }
  .contact .strong { font-weight: 700; }
  .facts { font-family: "Montserrat", Arial, sans-serif; fill: var(--ink); font-size: 7.6px; }
  .facts .strong { font-weight: 700; }
  .facts-title { font-family: "Montserrat", Arial, sans-serif; fill: #fff; font-size: 19px; font-weight: 400; }
  .facts-fine { font-family: "Montserrat", Arial, sans-serif; fill: var(--ink); font-size: 6.3px; }
  .rule { stroke: var(--ink); stroke-width: 1; }
  .leader { stroke: var(--ink); stroke-width: 0.8; stroke-dasharray: 0.8 1.6; }
</style>
</head>
<body>
<svg class="label" viewBox="0 0 956 435" xmlns="http://www.w3.org/2000/svg">
  <defs>
    <linearGradient id="produce-tone" x1="0" y1="0" x2="1" y2="1">
      <stop offset="0" stop-color="#8fc43a"/>
      <stop offset="0.5" stop-color="#9b2343"/>
      <stop offset="1" stop-color="#e9e2d6"/>
    </linearGradient>
  </defs>

  <!-- label paper -->
  <rect class="paper" x="0" y="0" width="956" height="435" fill="var(--paper)"/>

  <!-- bottom wave band -->
  <path class="band-yellow" d="M0 312 C 230 296, 430 338, 600 336 C 760 334, 860 318, 956 326 L956 435 L0 435 Z" fill="var(--band-yellow)"/>
  <path class="band-green" d="M0 322 C 230 306, 430 350, 600 348 C 760 346, 860 330, 956 338 L956 435 L0 435 Z" fill="var(--leaf-green)"/>

  <!-- left panel: story -->
  <text class="body-copy">
    <tspan x="30" y="46"><tspan class="strong">Brew Harbor</tspan> supplements are made</tspan>
    <tspan x="30" y="60">from the finest, purest ingredients</tspan>
    <tspan x="30" y="74">available. When you supplement your</tspan>
    <tspan x="30" y="88">diet to get vital nutrients, look no further</tspan>
    <tspan x="30" y="102">than <tspan class="strong">Brew Harbor</tspan> to ensure the best!</tspan>
    <tspan x="30" y="116">We  use vegetarian capsules with zero</tspan>
    <tspan x="30" y="130">fillers, so you can trust that you are</tspan>
    <tspan x="30" y="144">getting only what supports your health.</tspan>
  </text>

  <!-- quality badges (plain) -->
  <g class="badges" fill="var(--leaf-green)" stroke="#fff" stroke-width="2">
    <circle cx="66" cy="200" r="25"/>
    <circle cx="125" cy="200" r="25"/>
    <circle cx="184" cy="200" r="25"/>
    <circle cx="97" cy="258" r="25"/>
    <circle cx="155" cy="258" r="25"/>
  </g>

  <!-- contact box -->
  <rect class="contact-box" x="32" y="302" width="210" height="105" rx="6" fill="var(--leaf-green)" stroke="#fff" stroke-width="2"/>
  <text class="contact">
    <tspan x="45" y="322">Manufactured in the USA for :</tspan>
    <tspan x="45" y="336" class="strong">Brew Harbor</tspan>
    <tspan x="45" y="350">PO Box 1180, Mesa Verde AZ85001</tspan>
  </text>
  <line x1="34" y1="360" x2="240" y2="360" stroke="#fff" stroke-opacity="0.35"/>
  <g class="contact-icons" fill="#fff">
    <circle cx="50" cy="374" r="4"/>
    <circle cx="50" cy="390" r="4"/>
  </g>
  <text class="contact">
    <tspan x="60" y="378">555-014-0276</tspan>
    <tspan x="60" y="394">BREWHARBOR.COM</tspan>
  </text>

  <!-- front panel -->
  <text class="title" x="478" y="98" text-anchor="middle">RUBY ROOTS</text>
  <text class="tagline" x="478" y="126" text-anchor="middle">America’s top immune support</text>

  <rect class="hero-photo" x="324" y="145" width="325" height="285" rx="40" fill="url(#produce-tone)" role="img" aria-label="Photo of fresh red beets with leafy greens, a halved beet and garlic bulbs and cloves"/>

  <g class="count-badge">
    <rect x="629" y="165" width="62" height="120" rx="4" fill="var(--leaf-green)"/>
    <text class="count" x="660" y="203" text-anchor="middle" font-size="30">60</text>
    <text class="count" x="660" y="216" text-anchor="middle" font-size="6.5" font-weight="400">CAPSULES</text>
    <text class="count" x="660" y="249" text-anchor="middle" font-size="17">425mg</text>
    <text class="count" x="660" y="261" text-anchor="middle" font-size="6" font-weight="400">EACH</text>
  </g>

  <!-- supplement facts panel -->
  <g class="facts-panel">
    <rect x="696" y="47" width="234" height="340" rx="10" fill="#fff" stroke="var(--panel-black)" stroke-width="2"/>
    <path d="M696 80 V57 a10 10 0 0 1 10 -10 H920 a10 10 0 0 1 10 10 V80 Z" fill="var(--panel-black)"/>
    <text class="facts-title" x="813" y="71" text-anchor="middle">Supplement Facts</text>

    <text class="facts">
      <tspan x="716" y="93">Serving Size: 1 capsules</tspan>
      <tspan x="716" y="103">Servings per Container : <tspan class="strong">60</tspan></tspan>
    </text>
    <line class="rule" x1="697" y1="110" x2="929" y2="110"/>
    <text class="facts" x="716" y="126" font-size="8.6">Amount Per Serving</text>
    <line class="rule" x1="697" y1="136" x2="929" y2="136"/>

    <g class="facts-rows">
      <text class="facts" x="716" y="154">4:1 Beet extract</text>
      <line class="leader" x1="776" y1="154" x2="880" y2="154"/>
      <text class="facts" x="906" y="154" text-anchor="end">250mg ↑</text>

      <text class="facts" x="716" y="168">Allicin Garlic Extract</text>
      <line class="leader" x1="792" y1="168" x2="878" y2="168"/>
      <text class="facts" x="906" y="168" text-anchor="end">100mg ↑</text>

      <text class="facts" x="716" y="182">Vitamin C</text>
      <line class="leader" x1="752" y1="182" x2="880" y2="182"/>
      <text class="facts" x="898" y="182" text-anchor="end">50mg</text>

      <text class="facts" x="716" y="196">Zinc</text>
      <line class="leader" x1="734" y1="196" x2="880" y2="196"/>
      <text class="facts" x="898" y="196" text-anchor="end">25mg</text>

      <text class="facts" x="716" y="210">Vitamin D3</text>
      <line class="leader" x1="756" y1="210" x2="870" y2="210"/>
      <text class="facts" x="898" y="210" text-anchor="end">125mcg</text>
    </g>
    <line class="rule" x1="697" y1="222" x2="929" y2="222"/>
    <text class="facts" x="706" y="237">↑  Daily value(DV) not established.</text>
    <line class="rule" x1="697" y1="246" x2="929" y2="246"/>
    <text class="facts strong" x="813" y="259" text-anchor="middle">DO NOT USE IF TAMPER EVIDENT SEAL IS BROKEN</text>
    <line class="rule" x1="697" y1="268" x2="929" y2="268"/>

    <text class="facts">
      <tspan x="718" y="282"><tspan class="strong">Other ingredient :</tspan> veggie capsules</tspan>
      <tspan x="718" y="296" class="strong">SUGGESTED USE :</tspan>
      <tspan x="718" y="309">2 capsules daily with meals. As with any supplement,</tspan>
      <tspan x="718" y="318">consult your healthcare provider prior to use if you are</tspan>
      <tspan x="718" y="327">pregnant, nursing or taking any medication or have any</tspan>
      <tspan x="718" y="336">medical condition.</tspan>
    </text>
    <text class="facts-fine">
      <tspan x="718" y="351">*These statements have not been evaluated by the Food and</tspan>
      <tspan x="718" y="360">Drug Administration. This product is not intended to diagnose,</tspan>
      <tspan x="718" y="369">treat, cure or prevent any disease.</tspan>
    </text>
  </g>
</svg>
</body>
</html>
```